Entertainer/Dancer Business Cards

Corwin Latimer is an up and coming entertainer from Baltimore, Maryland currently relocating to Los Angeles, California for a dance opportunity at the renowned Marnie Holt Movement Loft.
This young man needs to promote himself and his skills in a populous and competitive city.
Hopefully, this card will set him apart from the tons of entertainers in L.A.
It will passed out to fellow entertainers, agents, and random people looking for talent.

I have uploaded an image of the dancer, it is not necessary to use this image; however it is in PSD format if one should decide to incorporate it somehow and would like to make changes.

Industry/Entity Type

Business

Contact Information for Business Card

Corwin Latimer
(line 1) Dancer Choreographer Instructor Singer/Songwriter
(line 2) Ballet-Modern-Urban
corwinlatimer00@quillpost.example
410-582-7146

Requirements
Nice to have

• Open to an all typography card.
Should not have
• No logo; just name: Corwin Latimer
Corwin is a guy (in case you were wondering :D )
Please no ballet/pointe shoes in design

```html
<!DOCTYPE html>
<html lang="en">
<head>
<meta charset="utf-8">
<title>Corwin Latimer — Business Card</title>
<link href="https://fonts.googleapis.com/css2?family=Josefin+Sans:wght@400&display=swap" rel="stylesheet">
<style>
  :root {
    --paper: #ffffff;
    --ink: #0a0a0a;
    --figure-tone-light: #f1f1f1;
    --figure-tone-dark: #d9d9d9;
  }
  html, body {
    margin: 0;
    padding: 0;
    overflow: hidden;
    background: var(--paper);
  }
  .card {
    position: relative;
    width: 1200px;
    height: 702px;
    background: var(--paper);
    color: var(--ink);
    font-family: "Josefin Sans", "Futura", sans-serif;
    font-variant: small-caps;
    overflow: hidden;
  }
  .contact {
    position: absolute;
    left: 39px;
    top: 36px;
    margin: 0;
  }
  .contact__name {
    margin: 0;
    font-size: 60px;
    font-weight: 400;
    line-height: 1;
    letter-spacing: 0.02em;
  }
  .contact__email,
  .contact__phone {
    display: block;
    font-style: normal;
    font-size: 40px;
    line-height: 1;
    letter-spacing: 0.01em;
    text-transform: lowercase;
  }
  .contact__email {
    margin-top: 22px;
    font-size: 34px;
  }
  .contact__phone {
    margin-top: 24px;
  }
  .dancer-figure {
    position: absolute;
    left: 622px;
    top: 56px;
    width: 528px;
    height: 372px;
    background: linear-gradient(160deg, var(--figure-tone-light), var(--figure-tone-dark));
  }
  .disciplines {
    position: absolute;
    left: 0;
    right: 0;
    top: 572px;
    margin: 0;
    text-align: center;
    font-size: 42px;
    line-height: 58px;
    letter-spacing: 0.015em;
  }
  .disciplines__line {
    display: block;
  }
</style>
</head>
<body>
  <main class="card">
    <div class="dancer-figure" role="img" aria-label="Minimal line illustration of a dancer with arms outstretched"></div>

    <header class="contact">
      <h1 class="contact__name">Corwin Latimer</h1>
      <address class="contact__email">corwinlatimer00@quillpost.example</address>
      <address class="contact__phone">410-582-7146</address>
    </header>

    <p class="disciplines">
      <span class="disciplines__line">Dancer Choreographer Instructor Singer/Songwriter</span>
      <span class="disciplines__line">Ballet-Modern-Urban</span>
    </p>
  </main>
</body>
</html>
```